Travel Itinerary Planning Website Redesign

We have built our own website for a travel itinerary planning service using Wix but are not professional designers. We need help getting over the finish line with a redesign of our website. <br/><br/>We like material design elements, icons and styling. The pages need to flow well one to another and evoke a sense of exclusivity, without giving the impression that it's unattainable. The website doesn't need to keep its current "boxy" format but instead should have a better aesthetic and flow. We're also looking for a complete redesign of the "How It Works" section (shown on two different pages of the website) to be more visually pleasing and easy to understand (maybe using icons or infographic style people). <br/><br/>We already have our logo and selected colors. The copy is also available on the live site as well. The redesign will focus on 4 pages: the homepage and the three service pages (one page per service). The website is currently live at www.trelmavista.com. Fonts should be Helvetica Bold, Regular and Light. Preferred color scheme is attached.

Target Market(s)

Ages 28-65, living in the US, mostly large cities with a desire for well planned, non-group travels

Industry/Entity Type

Travel Industry

Font styles to use
Other font styles liked:
• Helvetica

Colors

Designer to choose colors to be used in the design.

Requirements
Must have
• Make sure to use colors we provided in the attachment and what's on the current website
• Redesign "How it Works"
• Include ambassadors area
• Have a second page that showcases how the "Personal Trip Planning" page should look
Should not have
• No header menu needed for this project

```html
<!DOCTYPE html>
<html lang="en">
<head>
<meta charset="utf-8">
<title>Trelmavista — Personal Trip Planning</title>
<link href="https://fonts.googleapis.com/css2?family=Arimo:wght@400;700&display=swap" rel="stylesheet">
<style>
:root{
  --gold:#c59b3d;
  --brown:#6e4c1c;
  --brown-dark:#5a3d14;
  --ink:#333333;
  --muted:#666666;
  --page:#f7f7f7;
  --card:#ffffff;
  --sun:#fdd17c;
  --sun-deep:#f9c76a;
  --tick:#6e4c1c;
}
*{box-sizing:border-box;margin:0;padding:0}
html,body{width:1200px;height:4101px;overflow:hidden}
body{position:relative;background:var(--page);font-family:"Arimo",Helvetica,Arial,sans-serif;color:var(--ink)}
.abs{position:absolute}

/* hero */
.hero{left:0;top:0;width:1200px;height:367px;background:linear-gradient(180deg,#3d2b57 0%,#7c4a78 35%,#c66a7c 55%,#6d4a6e 72%,#2c2638 100%)}
.brand{left:95px;top:38px;color:#fff;font-weight:700;font-size:27px;letter-spacing:1px}
.nav{top:40px;color:#fff;font-size:12px;letter-spacing:.5px}
.nav.active{border-bottom:2px solid #fff;padding-bottom:6px}
.hero-title{left:0;width:1200px;text-align:center;color:#fff}
.hero-title.light{top:118px;font-size:57px;font-weight:400;letter-spacing:1px}
.hero-title.bold{top:176px;font-size:57px;font-weight:700}
.dots{top:334px;left:572px;display:flex;gap:5px}
.dots span{width:8px;height:8px;border-radius:50%;background:rgba(255,255,255,.5)}
.dots span.on{background:#fff}

/* intro */
.intro{left:76px;top:433px;width:1047px;height:237px;background:var(--card);box-shadow:0 2px 10px rgba(0,0,0,.12);border-radius:4px}
.intro h2{position:absolute;left:94px;top:64px;font-size:38px;font-weight:400;line-height:34px;color:var(--ink)}
.intro h2 b{color:var(--gold)}
.intro p{position:absolute;left:94px;top:145px;font-size:15px;color:var(--muted)}
.btn-dark{position:absolute;left:752px;top:85px;width:201px;height:47px;border:2px solid #222;border-radius:24px;font-size:15px;font-weight:700;color:#222;display:flex;align-items:center;justify-content:center;gap:10px}

/* section headings */
.eyebrow{font-size:14px;color:var(--ink);text-transform:uppercase}
.section-title{font-size:38px;font-weight:700;line-height:36px}
.gold{color:var(--gold)}
.brown{color:var(--brown)}

/* steps */
.illus{border-radius:28px}
.step-num{font-size:56px;font-weight:700;color:var(--gold);line-height:1}
.step-title{font-size:30px;line-height:33px;color:var(--brown);font-weight:400}
.step-title b{font-weight:700}
.step-text{font-size:21px;line-height:26px;color:var(--brown)}

/* plans */
.plans{left:0;top:2400px;width:1200px;height:723px;background:var(--sun)}
.plan{background:var(--card);border-radius:12px;box-shadow:0 3px 10px rgba(0,0,0,.12)}
.avatar{position:absolute;border-radius:50%;background:radial-gradient(circle at 50% 40%,#f8c050,#e9a83a)}
.plan h3{position:absolute;left:0;width:100%;text-align:center;font-size:22px;color:var(--brown);font-weight:700}
.plan .price{position:absolute;left:0;width:100%;text-align:center;font-size:12px;color:var(--brown)}
.plan ul{position:absolute;list-style:none}
.plan li{display:flex;align-items:center;gap:10px;font-size:9.5px;color:var(--brown)}
.plan li svg{flex:none}
.btn-line{position:absolute;border:2px solid var(--gold);border-radius:20px;color:var(--gold);font-size:11px;display:flex;align-items:center;justify-content:center;gap:10px;letter-spacing:.5px}

/* ambassadors */
.ambassadors{left:0;top:3123px;width:1200px;height:652px;background:#fcfcfc}
.photo{top:3380px;width:184px;height:182px}
.amb-name{top:3590px;width:250px;text-align:center;font-size:19px;font-weight:700;color:var(--brown)}
.amb-role{top:3614px;width:250px;text-align:center;font-size:18px;color:var(--gold)}

/* footer */
.footer{left:0;top:3775px;width:1200px;height:326px;background:var(--sun)}
.footer h4{font-size:14px;font-weight:700;color:var(--brown)}
.footer .item{font-size:12px;color:var(--brown)}
.divider{width:1px;background:var(--brown);opacity:.5}
</style>
</head>
<body>

<!-- hero -->
<div class="abs hero" role="img" aria-label="Sunset over a calm lake with a small wooden boat"></div>
<div class="abs brand">TRELMAVISTA</div>
<div class="abs nav active" style="left:897px">HOME</div>
<div class="abs nav" style="left:969px">ABOUT</div>
<div class="abs nav" style="left:1047px">CONTACT</div>
<div class="abs hero-title light">Keep it unique,</div>
<div class="abs hero-title bold">Keep it personal.</div>
<div class="abs dots"><span></span><span class="on"></span><span></span><span></span></div>

<!-- intro -->
<div class="abs intro">
  <h2>Based on your <b>needs,</b><br><b>budgets &amp; constraints.</b></h2>
  <p>Trelmavista travel engineer will work to create a tailored itinerary for you</p>
  <div class="btn-dark">Let’s get started!
    <svg width="13" height="13" viewBox="0 0 14 14"><circle cx="7" cy="7" r="6" fill="none" stroke="#222" stroke-width="1.5"/><path d="M5 7h4M7.5 5l2 2-2 2" fill="none" stroke="#222" stroke-width="1.4"/></svg>
  </div>
</div>

<!-- process -->
<div class="abs eyebrow" style="left:94px;top:739px">Our process</div>
<div class="abs section-title gold" style="left:94px;top:762px">How the<br>planning works</div>

<svg class="abs" style="left:0;top:0" width="1200" height="2400" aria-hidden="true">
  <g fill="none" stroke="var(--brown)" stroke-width="5" stroke-dasharray="16 12">
    <path d="M483 836 C600 835 720 880 710 1010"/>
    <path d="M665 1140 C560 1180 515 1260 520 1355"/>
    <path d="M550 1475 C590 1560 680 1530 735 1580 C760 1610 755 1640 735 1655"/>
    <path d="M468 1615 C510 1625 525 1650 525 1665"/>
    <path d="M175 1715 C110 1770 95 1840 180 1870 C280 1900 320 1960 318 2040"/>
    <path d="M328 2190 C360 2280 460 2310 600 2295 C660 2290 700 2275 735 2255"/>
  </g>
  <g fill="var(--brown)">
    <circle cx="710" cy="1016" r="9"/>
    <circle cx="520" cy="1358" r="9"/>
    <circle cx="734" cy="1657" r="9"/>
    <circle cx="318" cy="2046" r="9"/>
  </g>
</svg>

<!-- step 1 -->
<div class="abs illus" style="left:118px;top:935px;width:365px;height:270px;background:linear-gradient(180deg,#fdeccf,#f8c77a)" role="img" aria-label="Illustration of a phone sharing travel preferences among mountains"></div>
<div class="abs step-num" style="left:506px;top:1048px">1</div>
<div class="abs step-title" style="left:545px;top:1045px">SHARE YOUR<br><b>REFERENCES</b></div>
<div class="abs step-text" style="left:790px;top:1042px;width:270px">Connect with a Trelmavista Travel Engineer and discuss your expectations, needs, and budget.</div>

<!-- step 2 -->
<div class="abs illus" style="left:718px;top:1210px;width:364px;height:335px;background:linear-gradient(180deg,#fbf3e6 0%,#d9a64a 50%,#f7b98a 100%)" role="img" aria-label="Illustration of a travel engineer writing a day-by-day plan at a laptop"></div>
<div class="abs step-num" style="left:212px;top:1377px">2</div>
<div class="abs step-title" style="left:260px;top:1375px">LET US DO<br><b>THE WORK</b></div>
<div class="abs step-text" style="left:450px;top:1375px;width:260px">Our teams will be hard at work handcrafting plans, ahead of your next departure.</div>

<!-- step 3 -->
<div class="abs illus" style="left:160px;top:1525px;width:318px;height:425px;background:linear-gradient(180deg,#bfeaf7 0%,#f6c26b 55%,#f7b792 100%)" role="img" aria-label="Illustration of a hand holding a phone with a digital itinerary"></div>
<div class="abs step-num" style="left:504px;top:1683px">3</div>
<div class="abs step-title" style="left:552px;top:1680px">OBTAIN YOUR<br><b>ITINERARY</b></div>
<div class="abs step-text" style="left:552px;top:1760px;width:270px">Access a personal, digital itinerary through your favorite devices.</div>

<!-- step 4 -->
<div class="abs illus" style="left:734px;top:1936px;width:334px;height:344px;border-radius:70px;background:linear-gradient(180deg,#aeeaf7 0%,#d7f3f8 50%,#f9d59a 60%,#f6c27a 100%)" role="img" aria-label="Illustration of a map pin with a money symbol"></div>
<div class="abs step-num" style="left:190px;top:2088px">4</div>
<div class="abs step-title" style="left:238px;top:2085px">SAVE TIME<br><b>AND MONEY</b></div>
<div class="abs step-text" style="left:450px;top:2065px;width:250px">Avoid common mistakes and travel planning frustrations. We’ve got you covered.</div>

<!-- plans -->
<div class="abs plans"></div>
<div class="abs eyebrow" style="left:94px;top:2453px">Select a suitable plan for you</div>
<div class="abs section-title brown" style="left:94px;top:2475px">Plans &amp; Pricing</div>

<div class="abs plan" style="left:258px;top:2598px;width:294px;height:439px">
  <div class="avatar" style="left:95px;top:12px;width:104px;height:104px" role="img" aria-label="Mascot character in sunglasses and scarf"></div>
  <h3 style="top:155px">Standard Trip</h3>
  <div class="price" style="top:180px"><b>30 USD</b> / Travel Day</div>
  <ul style="left:42px;top:202px">
    <li style="height:25.5px"><svg width="12" height="12"><circle cx="6" cy="6" r="6" fill="var(--tick)"/><path d="M3 6l2 2 4-4" stroke="#fff" stroke-width="1.5" fill="none"/></svg>Personalized, hand-crafted itinerary</li>
    <li style="height:25.5px"><svg width="12" height="12"><circle cx="6" cy="6" r="6" fill="var(--tick)"/><path d="M3 6l2 2 4-4" stroke="#fff" stroke-width="1.5" fill="none"/></svg>Unlimited chat with a travel engineer</li>
    <li style="height:25.5px"><svg width="12" height="12"><circle cx="6" cy="6" r="6" fill="var(--tick)"/><path d="M3 6l2 2 4-4" stroke="#fff" stroke-width="1.5" fill="none"/></svg>20-minute kick-off call with Trelmavista</li>
    <li style="height:25.5px"><svg width="12" height="12"><circle cx="6" cy="6" r="6" fill="var(--tick)"/><path d="M3 6l2 2 4-4" stroke="#fff" stroke-width="1.5" fill="none"/></svg>Lodging, food &amp; entertainment recommendations</li>
    <li style="height:25.5px"><svg width="12" height="12"><circle cx="6" cy="6" r="6" fill="var(--tick)"/><path d="M3 6l2 2 4-4" stroke="#fff" stroke-width="1.5" fill="none"/></svg>Access to user-friendly, online itinerary tool</li>
    <li style="height:25.5px"><svg width="12" height="12"><circle cx="6" cy="6" r="6" fill="var(--tick)"/><path d="M3 6l2 2 4-4" stroke="#fff" stroke-width="1.5" fill="none"/></svg>Initial itinerary delivered in 2 weeks</li>
  </ul>
  <div class="btn-line" style="left:68px;top:380px;width:158px;height:35px">GET STARTED
    <svg width="12" height="12" viewBox="0 0 14 14"><circle cx="7" cy="7" r="6" fill="none" stroke="var(--gold)" stroke-width="1.5"/><path d="M5 7h4M7.5 5l2 2-2 2" fill="none" stroke="var(--gold)" stroke-width="1.4"/></svg>
  </div>
</div>

<div class="abs plan" style="left:588px;top:2560px;width:316px;height:497px">
  <div class="avatar" style="left:100px;top:8px;width:116px;height:128px;border-radius:50% 50% 46% 46%" role="img" aria-label="Mascot character in an explorer hat"></div>
  <h3 style="top:165px">Premium Trip</h3>
  <div class="price" style="top:190px"><b>60 USD</b> / Travel Day</div>
  <ul style="left:42px;top:220px">
    <li style="height:31px;font-weight:700"><svg width="12" height="12"><circle cx="6" cy="6" r="6" fill="var(--tick)"/><path d="M3 6l2 2 4-4" stroke="#fff" stroke-width="1.5" fill="none"/></svg>Standard Plan + the following premium services:</li>
    <li style="height:31px"><svg width="12" height="12"><circle cx="6" cy="6" r="6" fill="var(--tick)"/><path d="M3 6l2 2 4-4" stroke="#fff" stroke-width="1.5" fill="none"/></svg>Flight bookings</li>
    <li style="height:31px"><svg width="12" height="12"><circle cx="6" cy="6" r="6" fill="var(--tick)"/><path d="M3 6l2 2 4-4" stroke="#fff" stroke-width="1.5" fill="none"/></svg>Accommodations negotiation and reservations</li>
    <li style="height:31px"><svg width="12" height="12"><circle cx="6" cy="6" r="6" fill="var(--tick)"/><path d="M3 6l2 2 4-4" stroke="#fff" stroke-width="1.5" fill="none"/></svg>Restaurant and activity reservations</li>
    <li style="height:31px"><svg width="12" height="12"><circle cx="6" cy="6" r="6" fill="var(--tick)"/><path d="M3 6l2 2 4-4" stroke="#fff" stroke-width="1.5" fill="none"/></svg>Concierge service</li>
    <li style="height:31px"><svg width="12" height="12"><circle cx="6" cy="6" r="6" fill="var(--tick)"/><path d="M3 6l2 2 4-4" stroke="#fff" stroke-width="1.5" fill="none"/></svg>Traveler’s itinerary booklet</li>
  </ul>
  <div class="btn-line" style="left:80px;top:425px;width:158px;height:36px">GET STARTED
    <svg width="12" height="12" viewBox="0 0 14 14"><circle cx="7" cy="7" r="6" fill="none" stroke="var(--gold)" stroke-width="1.5"/><path d="M5 7h4M7.5 5l2 2-2 2" fill="none" stroke="var(--gold)" stroke-width="1.4"/></svg>
  </div>
</div>

<!-- ambassadors -->
<div class="abs ambassadors"></div>
<div class="abs" style="left:94px;top:3177px;font-size:12px;line-height:14px">EXPERIENCES CURATED<br>WITH INSPIRATION FROM</div>
<div class="abs section-title brown" style="left:94px;top:3210px">Our Brand<br>Ambassadors</div>
<div class="abs" style="left:94px;top:3297px;font-size:11.5px;line-height:14px">Get a personalised list of the things you want to do<br>and the places you want to visit.</div>

<svg class="abs" style="left:90px;top:3482px" width="20" height="30" aria-hidden="true"><path d="M15 3L4 15l11 12" fill="none" stroke="#333" stroke-width="2.5"/></svg>
<svg class="abs" style="left:1088px;top:3482px" width="20" height="30" aria-hidden="true"><path d="M5 3l11 12L5 27" fill="none" stroke="#333" stroke-width="2.5"/></svg>

<div class="abs photo" style="left:144px;background:linear-gradient(180deg,#8fb2d6,#6b7f9a)" role="img" aria-label="Portrait of ambassador Conrad Halvorsen"></div>
<div class="abs photo" style="left:397px;background:linear-gradient(180deg,#efe6dc,#c9b5a3)" role="img" aria-label="Portrait of ambassador Elise Ravenel"></div>
<div class="abs photo" style="left:638px;width:187px;background:linear-gradient(180deg,#5e5a52,#3e3a36)" role="img" aria-label="Portrait of ambassador Mathis Dorvalle"></div>
<div class="abs photo" style="left:876px;width:183px;background:linear-gradient(180deg,#e8e3dc,#7a6355)" role="img" aria-label="Portrait of ambassador Livia Marchetti"></div>

<div class="abs amb-name" style="left:111px">CONRAD HALVORSEN</div>
<div class="abs amb-role" style="left:111px">Author &amp; TV Personality</div>
<div class="abs amb-name" style="left:364px">ELISE RAVENEL</div>
<div class="abs amb-role" style="left:364px">French Lifestyle Influencer</div>
<div class="abs amb-name" style="left:607px">MATHIS DORVALLE</div>
<div class="abs amb-role" style="left:607px">Founder &amp; CEO</div>
<div class="abs amb-name" style="left:843px">LIVIA MARCHETTI</div>
<div class="abs amb-role" style="left:843px">Italian Singer</div>

<div class="abs btn-line" style="left:877px;top:3683px;width:182px;height:37px">View all ambassadors
  <svg width="12" height="12" viewBox="0 0 14 14"><circle cx="7" cy="7" r="6" fill="none" stroke="var(--gold)" stroke-width="1.5"/><path d="M5 7h4M7.5 5l2 2-2 2" fill="none" stroke="var(--gold)" stroke-width="1.4"/></svg>
</div>

<!-- footer -->
<div class="abs footer"></div>
<div class="abs" style="left:98px;top:3990px;font-size:19px;font-weight:700;color:var(--brown)">TRELMAVISTA</div>

<div class="abs divider" style="left:286px;top:3845px;height:180px"></div>
<div class="abs divider" style="left:542px;top:3845px;height:180px"></div>
<div class="abs divider" style="left:843px;top:3845px;height:180px"></div>

<h4 class="abs" style="left:316px;top:3843px;font-size:14px;font-weight:700;color:var(--brown)">MENU</h4>
<div class="abs footer-menu" style="left:316px;top:3872px;font-size:12px;line-height:28.3px;color:var(--brown)">
  PERSONAL TRIP PLANNING<br>BUSINESS TRIP PLANNING<br>OVERSEAS EVENT PLANNING<br>FREE TRAVEL RESOURCES<br>TERMS AND CONDITIONS<br>PRIVACY POLICY
</div>

<h4 class="abs" style="left:588px;top:3843px;font-size:14px;font-weight:700;color:var(--brown)">WHO WE ARE</h4>
<div class="abs" style="left:588px;top:3870px;width:230px;font-size:12px;line-height:17px;color:var(--brown)">Trelmavista’s mission is to engineer personalized, handcrafted travel itineraries and event plans for travelers worldwide</div>
<div class="abs" style="left:588px;top:3982px;font-size:12px;line-height:28.3px;color:var(--brown)">SAMPLE LINK<br>SAMPLE LINK</div>

<h4 class="abs" style="left:873px;top:3843px;font-size:14px;font-weight:700;color:var(--brown)">WE’RE SOCIAL!</h4>
<div class="abs" style="left:873px;top:3868px;font-size:12px;line-height:29px;color:var(--brown)">
  <div style="display:flex;align-items:center;gap:8px"><svg width="16" height="16"><circle cx="8" cy="8" r="6.5" fill="none" stroke="var(--brown)" stroke-width="1.6"/></svg>FOLLOW US ON SNAPWALL</div>
  <div style="display:flex;align-items:center;gap:8px"><svg width="16" height="16"><circle cx="8" cy="8" r="7.5" fill="var(--brown)"/><text x="8" y="12" text-anchor="middle" font-size="11" font-weight="700" fill="#fdd17c" font-family="Arimo,sans-serif">?</text></svg>GOT QUESTIONS? CONTACT US.</div>
</div>
<div class="abs" style="left:873px;top:4012px;font-size:11px;color:var(--brown)">©2020 Trelmavista I All Rights Reserved.</div>

</body>
</html>
```